Super-fantastic-interesting infographic of terribly boring content

-Looking to provide a visually engaging snapshot of the average Canadian investor.
-Help people compare their personal financial situation against the infographic (Average).
-We want viewers to feel engaged and interested in the info presented, not confused and irritated.

Data points to present:

The average Canadian snapshot:
* Average Canadian household Income in 2016: $76,900
* Median Net Worth of Canadian families in 2016: $295,100
* Average annual household expenditures on goods a& services: $62,183
* Median value in principal residence: $349,000
* Highest net annual savings amount (Age 35-44): $10,120
* Number of Canadian families holding a mortgage: 38.4%
* Median Mortgage value of Principal residence: $190,000
* Debt to disposable income ratio average: 172.1
* Total value of all assets held by Canadians in 2016: 12 Trillion dollars
* The principal residence was the single largest asset held (of the 12 Trillion): 32%
* Private pensions was the 2nd largest grouping of assets at 29.2%
* The average borrowing rate for Canadian mortgages: 2.94%
* 74% were fixed rate, 21% were variable and 5% blended.
* 48% of Canadians do not save or invest at all
* 54% of Canadians do not budget regularly
* 1 in 3 Canadians have lost at least 20% in one year
* 51% of Canadians took NO ACTION after losing at least 20% in one year.
* 22% of those people either, hired or fired an advisor

Financial advice landscape:
* # of households in Canada: 13,300,000
* Households with an advisor 5,300,000
* % of households dissatisfied with existing advisor 1,100,000

Target Market(s)

Investors, ages 22-55

Industry/Entity Type

Financial

Font styles to use
Sans Serif

Colors

Designer to choose colors to be used in the design.

Requirements
Must have
• Header: Financial landscape of the average Canadian
Nice to have
• There is a lot of numbers and percentages, find a way to deliver the info using a mix of images, numbers, pictures etc.

```html
<!DOCTYPE html>
<html lang="en">
<head>
<meta charset="utf-8">
<title>Financial Landscape of average Canadian 2016-2017</title>
<link href="https://fonts.googleapis.com/css2?family=Roboto+Condensed:wght@300;400;700&family=Roboto:wght@300;400;500;700&display=swap" rel="stylesheet">
<style>
:root{
  --plum:#5f3f5c;
  --green:#1db46a;
  --red:#d3262c;
  --blue-sign:#4b8fae;
  --teal:#7dcbc0;
  --lavender:#8088c6;
  --forest:#1aa556;
  --tag:#f4b41a;
  --paper:#fdf19a;
  --paper-curl:#f6bb3f;
  --slate:#4f6e80;
  --steel:#4d7fa0;
  --mort-purple:#6b4f8f;
  --mort-blue:#2f74b8;
  --mort-lilac:#8d74b5;
  --ink:#444;
  --white:#fff;
  --pale:#e8efee;
  --grey:#9aa7b0;
}
*{margin:0;padding:0;box-sizing:border-box}
html,body{width:1200px;height:780px;overflow:hidden;background:var(--plum)}
body{font-family:"Roboto",Arial,sans-serif;color:var(--white)}
.canvas{position:relative;width:1200px;height:780px;background:var(--plum);overflow:hidden}
.abs{position:absolute}
.cond{font-family:"Roboto Condensed","Arial Narrow",sans-serif}

/* header */
.title{left:30px;top:22px;font-family:"Roboto Condensed",sans-serif;font-weight:700;color:var(--green);font-size:60px;line-height:56px;letter-spacing:-2px}
.art{border-radius:6px}
.subtitle{right:26px;top:22px;text-align:right;font-family:"Roboto Condensed",sans-serif;font-weight:700;line-height:34px}
.subtitle .of{color:var(--red);font-size:37px;letter-spacing:-1px}
.subtitle .yr{color:var(--white);font-size:40px;line-height:46px;margin-top:4px}
.rule{left:28px;top:146px;width:1144px;border-top:1.5px dashed rgba(255,255,255,.6)}

/* advice */
.advice-frame{left:230px;top:182px;width:580px;height:230px;border:1.5px solid var(--white)}
.advice-title{left:248px;top:167px;background:var(--plum);padding:0 8px;font-family:"Roboto Condensed",sans-serif;font-weight:300;font-size:23px;letter-spacing:-.5px}
.pct{font-family:"Roboto Condensed",sans-serif;color:#2f86c9;font-size:9px;line-height:10px;z-index:2}
.pct b{font-size:16px;line-height:18px;display:block;font-weight:700}
.asset-leaf{left:104px;top:232px;width:60px;height:82px;border-radius:40%;background:linear-gradient(90deg,#f08a82 50%,#d8343a 50%);z-index:1}
.trillion{left:34px;top:324px;width:182px;height:64px;background:var(--white);border-radius:10px;text-align:center;color:var(--mort-blue);padding-top:4px}
.trillion .big{font-family:"Roboto Condensed",sans-serif;font-weight:700;font-size:28px;line-height:30px}
.trillion .small{font-size:11.5px;line-height:13px;font-weight:300;color:#2a5e94}
.legend{left:242px;top:312px;width:252px;height:90px;background:var(--white);border-radius:3px;padding:4px 8px 0 34px;color:var(--ink)}
.legend .row{height:28px;position:relative}
.legend .row i{position:absolute;left:-28px;top:3px;width:20px;height:18px;border-radius:2px}
.legend .num{font-family:"Roboto Condensed",sans-serif;font-weight:700;font-size:14px;line-height:14px;color:#555}
.legend .lbl{font-size:8.5px;line-height:10px;font-weight:300;color:#666}
.legend .red .num,.legend .red .lbl{color:var(--red)}
.sign{left:509px;top:210px;width:181px;height:102px;background:var(--blue-sign);padding:14px 0 0 16px}
.sign .n{font-family:"Roboto Condensed",sans-serif;font-weight:700;font-size:31px;line-height:32px}
.sign .t{font-family:"Roboto Condensed",sans-serif;font-size:22px;line-height:20px}
.card{padding:8px 6px 0 8px;line-height:1}
.card .v{font-family:"Roboto Condensed",sans-serif;font-weight:700;font-size:23px}
.card .c{font-size:7.5px;line-height:8px;font-weight:300;margin-top:2px}
.tag{position:absolute;right:0;top:0;background:var(--tag);color:#6a3a0a;font-family:"Roboto Condensed",sans-serif;font-weight:700;font-size:11px;padding:1px 5px}

/* mortgage */
.mort-cap{font-family:"Roboto Condensed",sans-serif;font-size:13.5px;font-weight:300;color:#555}
.mort-cap b{font-weight:700}
.rates{left:850px;top:508px;width:157px;height:66px;border:1px dashed var(--steel);padding:4px 0 0 10px;font-family:"Roboto Condensed",sans-serif;font-size:15px;line-height:19px;color:#6c6c80}

/* habits */
.habits{left:22px;top:422px;width:728px;height:316px;background:var(--slate)}
.habit-tab{left:616px;top:422px;width:134px;height:74px;background:var(--paper);color:var(--steel);text-align:right;padding:6px 14px 0 0;font-family:"Roboto Condensed",sans-serif;font-weight:700;font-size:27px;line-height:29px}
.stat{text-align:center;width:170px}
.stat .n{font-family:"Roboto Condensed",sans-serif;font-weight:700;font-size:37px;line-height:38px}
.stat .c{font-family:"Roboto Condensed",sans-serif;font-weight:300;font-size:15px;line-height:16px}
.ratio{left:646px;top:510px;width:92px;text-align:center}
.ratio .n{font-family:"Roboto Condensed",sans-serif;font-weight:700;font-size:31px;line-height:34px}
.ratio .c{font-family:"Roboto Condensed",sans-serif;font-weight:300;font-size:12.5px;line-height:14px}
.box51{left:644px;top:602px;width:90px;height:54px;background:var(--red);text-align:center;padding-top:6px}
.box22{left:644px;top:658px;width:90px;height:56px;background:var(--white);color:var(--red);text-align:center;padding-top:4px}
.box51 .n,.box22 .n{font-family:"Roboto Condensed",sans-serif;font-weight:700;font-size:26px;line-height:26px}
.box51 .c{font-size:10px;font-weight:700}
.box22 .c{font-size:10px;line-height:11px;font-weight:300}

.brand{left:860px;top:670px;width:312px;height:110px;background:var(--white);display:flex;align-items:center;justify-content:center;gap:12px}
.brand .dot{width:40px;height:40px;border-radius:50%;background:#2b63b8}
.brand .name{font-family:"Roboto",sans-serif;font-weight:400;font-size:32px;color:#333}
</style>
</head>
<body>
<div class="canvas">

  <!-- header -->
  <h1 class="abs title">FINANCIAL<br>LANDSCAPE</h1>
  <div class="abs art" role="img" aria-label="Illustration of banknotes and stacked gold coins" style="left:372px;top:62px;width:152px;height:64px;background:linear-gradient(90deg,#f3b93a,#7ab65a 35%,#7ab65a 65%,#f3b93a)"></div>
  <div class="abs art" role="img" aria-label="Illustration of a grey safe" style="left:538px;top:52px;width:68px;height:70px;background:#8ea0a8"></div>
  <div class="abs art" role="img" aria-label="Illustration of a blue house" style="left:628px;top:52px;width:76px;height:70px;background:linear-gradient(180deg,#4a8a55 0 30%,#a9c1e0 30%)"></div>
  <div class="abs" role="img" aria-label="Red maple leaf" style="left:900px;top:42px;width:88px;height:86px;border-radius:40%;background:var(--red)"></div>
  <div class="abs subtitle">
    <div class="of">of average<br>Canadian</div>
    <div class="yr">2016-2017</div>
  </div>
  <div class="abs rule"></div>

  <!-- financial advice landscape -->
  <div class="abs advice-frame"></div>
  <h2 class="abs advice-title">FINANCIAL ADVICE LANDSCAPE</h2>

  <div class="abs pct" style="left:36px;top:204px;width:64px;text-align:right"><b>29.2%</b>of assets being held by <strong>private pensions</strong></div>
  <div class="abs pct" style="left:168px;top:200px;width:60px"><b>32%</b>of assets being held by <strong>principal residences</strong></div>
  <div class="abs asset-leaf" role="img" aria-label="Maple leaf split into shares of assets"></div>
  <div class="abs trillion">
    <div class="big">$12 TRILLION</div>
    <div class="small">total value of assets<br>Canadian holds in 2016</div>
  </div>

  <div class="abs" role="img" aria-label="Ten house icons, some marked with a frown for dissatisfied households" style="left:240px;top:212px;width:256px;height:88px;border-radius:4px;background:linear-gradient(90deg,#a8c2e4 0 40%,#e3d6a0 40%)"></div>

  <div class="abs legend">
    <div class="row"><i style="background:#a8c2e4"></i><div class="num">5,300,000</div><div class="lbl">households <b>with</b> financial advisor</div></div>
    <div class="row red"><i style="background:#d8343a"></i><div class="num">8,000,000</div><div class="lbl">households <b>without</b> financial advisor</div></div>
    <div class="row"><i style="background:#c9cbb0"></i><div class="num">1,100,000</div><div class="lbl">dissatisfied households <b>with</b> current financial advisor</div></div>
  </div>

  <svg class="abs" style="left:500px;top:190px" width="310" height="220" viewBox="0 0 310 220">
    <line x1="98" y1="120" x2="98" y2="210" stroke="#c9cdd2" stroke-width="5"/>
    <line x1="190" y1="30" x2="210" y2="30" stroke="#c9cdd2" stroke-width="4"/>
    <line x1="190" y1="100" x2="210" y2="75" stroke="#c9cdd2" stroke-width="4"/>
    <line x1="190" y1="115" x2="210" y2="148" stroke="#c9cdd2" stroke-width="4"/>
  </svg>
  <div class="abs sign">
    <div class="n">13,300,000</div>
    <div class="t">households<br>in Canada</div>
  </div>
  <div class="abs card" style="left:502px;top:330px;width:96px;height:46px;background:var(--lavender);text-align:center">
    <div class="v" style="font-size:21px">$349,000</div>
    <div class="c">median value in<br>principal residence</div>
  </div>
  <div class="abs card" style="left:701px;top:190px;width:97px;height:60px;background:var(--teal);color:#4d6a70">
    <span class="tag">2016</span>
    <div class="v" style="margin-top:10px">$76,900</div>
    <div class="c">average annual<br>household income</div>
  </div>
  <div class="abs card" style="left:701px;top:258px;width:97px;height:66px;background:var(--red)">
    <span class="tag">2016</span>
    <div class="v" style="margin-top:10px">$62,183</div>
    <div class="c">average annual household expenditures (goods &amp; services)</div>
  </div>
  <div class="abs card" style="left:701px;top:330px;width:97px;height:60px;background:var(--forest)">
    <span class="tag">2016</span>
    <div class="v" style="margin-top:10px">$295,100</div>
    <div class="c">median net worth<br>of Canadian families</div>
  </div>

  <!-- mortgage -->
  <svg class="abs" style="left:760px;top:180px" width="412" height="440" viewBox="0 0 412 440">
    <path d="M64 0 H412 V440 H120 Q70 440 66 390 Q64 320 10 330 Q40 300 64 280 Z" fill="var(--paper)"/>
    <path d="M4 330 Q60 310 66 390 Q70 440 120 440 Q30 440 4 330 Z" fill="var(--paper-curl)"/>
  </svg>
  <div class="abs cond" style="left:854px;top:204px;color:var(--steel);font-size:17px;font-weight:700">about</div>
  <div class="abs cond" style="left:852px;top:214px;color:var(--steel);font-size:50px;font-weight:700;letter-spacing:-1px">MORTGAGE</div>
  <div class="abs" role="img" aria-label="House icon in a yellow circle" style="left:1086px;top:212px;width:64px;height:64px;border-radius:50%;background:#f6c030;border:3px solid #f9d66a"></div>
  <div class="abs" style="left:852px;top:276px;width:218px;border-top:1px dashed var(--steel)"></div>

  <div class="abs cond" style="left:850px;top:280px;color:var(--mort-purple);font-size:42px;font-weight:400">38.4%</div>
  <div class="abs mort-cap" style="left:850px;top:326px">number of Canadian families <b>holding a mortgage</b></div>
  <div class="abs cond" style="left:846px;top:356px;color:var(--mort-blue);font-size:48px;font-weight:700;letter-spacing:-1px">$190,000</div>
  <div class="abs mort-cap" style="left:850px;top:406px">median mortgage value of principal residence.</div>
  <div class="abs cond" style="left:850px;top:442px;color:var(--mort-lilac);font-size:42px;font-weight:400">2.94%</div>
  <div class="abs mort-cap" style="left:853px;top:490px">average borrowing rate for Canadian mortgages</div>
  <div class="abs rates">74% fixed rate<br>21% variable rate<br>5% blended rate</div>

  <!-- finance habit -->
  <div class="abs habits"></div>
  <div class="abs habit-tab">FINANCE<br>HABIT</div>

  <div class="abs" style="left:39px;top:482px;width:140px;height:140px;border-radius:50%;background:var(--red)"></div>
  <div class="abs" style="left:51px;top:494px;width:116px;height:116px;border-radius:50%;background:var(--white)"></div>
  <div class="abs art" role="img" aria-label="Safe with banknote going in" style="left:76px;top:508px;width:66px;height:88px;background:#8ea0a8"></div>
  <div class="abs stat" style="left:24px;top:634px">
    <div class="n">48%</div>
    <div class="c">do not save or<br>do not invest<br><b style="font-weight:700">at all.</b></div>
  </div>

  <div class="abs" style="left:204px;top:482px;width:140px;height:140px;border-radius:50%;background:var(--red)"></div>
  <div class="abs art" role="img" aria-label="Torn budget sheet with banknote" style="left:220px;top:491px;width:110px;height:126px;border-radius:0;background:#f8ef92"></div>
  <div class="abs stat" style="left:189px;top:634px">
    <div class="n">54%</div>
    <div class="c">do not budget<br>regularly</div>
  </div>

  <div class="abs" style="left:363px;top:482px;width:140px;height:140px;border-radius:50%;background:var(--pale)"></div>
  <div class="abs cond" style="left:363px;top:490px;width:140px;text-align:center;color:#5f8fae;font-size:16px;line-height:17px">age<br><b style="font-size:17px">35-44</b></div>
  <div class="abs art" role="img" aria-label="Safe holding banknotes" style="left:399px;top:532px;width:68px;height:68px;background:#8ea0a8"></div>
  <div class="abs stat" style="left:343px;top:630px;width:180px">
    <div class="n">$10,120</div>
    <div class="c">highest net<br>annual savings<br>in 2016</div>
  </div>

  <div class="abs" role="img" aria-label="Three figures, one outlined and confused about losing 20%" style="left:512px;top:486px;width:120px;height:122px;border-radius:6px;background:linear-gradient(90deg,rgba(255,255,255,.85) 0 40%,var(--red) 40%)"></div>
  <div class="abs stat" style="left:497px;top:630px">
    <div class="n">1 of 3</div>
    <div class="c">have lost 20%<br>of their assets<br>in one year</div>
  </div>

  <div class="abs ratio">
    <div class="n">172:1</div>
    <div class="c">debt to<br>disposable<br>income ratio</div>
  </div>
  <div class="abs box51"><div class="n">51%</div><div class="c">do NOTHING!</div></div>
  <div class="abs box22"><div class="n">22%</div><div class="c">hired/fired<br>financial advisor</div></div>

  <!-- brand -->
  <div class="abs brand">
    <span class="dot"></span>
    <span class="name">Ledgerline</span>
  </div>
</div>
</body>
</html>
```